Construction Company Business Card

We need a logo and a business card for our new construction company. We are based in Veskara, Amaruland. Our company specializes in the design and construction of high end residential homes and commercial buildings. We want a modern and elegant logo. Preferred colours are gun metal grey/ slate (or anything along those lines) and red as a feature. We are however open to any ideas. The design should communicate prestige and elegance in the work that we undertake.
The uploaded sketch is just something we were pondering with but you can completely disregard it.

Industry/Entity Type

Construction

Contact Information for Business Card

Company Name: Tabor Vask

Company Address:
Tabor Vask
P.O.Box 2871-00529
Lindoro, Veskara, 00529
Amaruland

Name on business card: Tabor V. Osumba

```html
<!DOCTYPE html>
<html lang="en">
<head>
<meta charset="utf-8">
<title>Tabor Vask – Business Card</title>
<link href="https://fonts.googleapis.com/css2?family=Ubuntu:wght@500;700&display=swap" rel="stylesheet">
<style>
  :root {
    --page-bg: #e4e4e6;
    --navy: #2c2a6b;
    --lavender: #8f8fd6;
    --card-white: #ffffff;
    --drawing-grey: #dcdde0;
    --ink: #141414;
    --label-red: #8b1a1a;
    --brand: #7a3f97;
    --on-navy: #ffffff;
  }
  html, body {
    margin: 0;
    padding: 0;
    width: 1200px;
    height: 1200px;
    overflow: hidden;
    background: var(--page-bg);
  }
  .card {
    position: absolute;
    left: 100px;
    top: 310px;
    width: 1000px;
    height: 580px;
    background: var(--card-white);
    overflow: hidden;
    box-shadow: 0 10px 30px rgba(0,0,0,0.18);
    font-family: "Ubuntu", sans-serif;
  }
  .blueprint-area {
    position: absolute;
    left: 0;
    top: 60px;
    width: 1000px;
    height: 400px;
    background:
      radial-gradient(ellipse at 78% 40%, rgba(255,255,255,0.95) 0%, rgba(255,255,255,0) 45%),
      linear-gradient(120deg, var(--drawing-grey) 0%, #f2f2f4 40%, #e3e4e7 65%, #f7f7f8 100%);
  }
  .bands {
    position: absolute;
    inset: 0;
  }
  .holder-name {
    position: absolute;
    left: 56px;
    top: 46px;
    margin: 0;
    color: var(--on-navy);
    font-weight: 700;
    font-size: 40px;
    letter-spacing: 2px;
  }
  .brand-name {
    position: absolute;
    right: 44px;
    top: 72px;
    display: flex;
    align-items: center;
    gap: 14px;
    color: var(--brand);
    font-weight: 700;
    font-size: 40px;
    letter-spacing: 1px;
    line-height: 1;
  }
  .brand-mark {
    width: 22px;
    height: 22px;
    background: var(--brand);
  }
  .contact {
    position: absolute;
    left: 60px;
    top: 248px;
    color: var(--ink);
    font-weight: 500;
    font-size: 24px;
    letter-spacing: 1px;
    line-height: 38px;
  }
  .contact p { margin: 0; }
  .contact .address { margin-bottom: 12px; }
  .contact .label { color: var(--label-red); }
  .tagline {
    position: absolute;
    left: 0;
    right: 0;
    top: 490px;
    margin: 0;
    text-align: center;
    color: var(--on-navy);
    font-weight: 500;
    font-size: 21px;
    letter-spacing: 1px;
    line-height: 30px;
  }
</style>
</head>
<body>
  <div class="card">
    <div class="blueprint-area" role="img" aria-label="Faint architectural blueprint drawings of building plans"></div>

    <svg class="bands" width="1000" height="580" viewBox="0 0 1000 580" aria-hidden="true">
      <polygon points="0,0 1000,0 1000,52 600,52 520,128 0,128" fill="var(--navy)"/>
      <polyline points="0,134 524,134 604,58 1000,58" fill="none" stroke="var(--lavender)" stroke-width="5"/>
      <line x1="0" y1="458" x2="1000" y2="458" stroke="var(--lavender)" stroke-width="6"/>
      <rect x="0" y="462" width="1000" height="118" fill="var(--navy)"/>
    </svg>

    <h1 class="holder-name">TABOR V. OSUMBA</h1>

    <div class="brand-name">
      <span class="brand-mark"></span>
      <span>TABOR VASK</span>
    </div>

    <div class="contact">
      <p class="address">TABOR VASK, P.O.BOX 2871-00529,<br>LINDORO, VESKARA, 00529 AMARULAND</p>
      <p><span class="label">EMAIL:</span> OFFICE@TABORVASK.CO.KE</p>
      <p><span class="label">PHONE NUMBER:</span> 0417-5718264091</p>
    </div>

    <p class="tagline">SPECIALIZES IN THE DESIGN AND CONSTRUCTION OF HIGH END RESIDENTIAL HOMES<br>AND COMMERCIAL BUILDINGS</p>
  </div>
</body>
</html>
```